BRV Stationary
BRV All The Way!
Corporate
Dale Orwick
CEO
2380 Tallow St. Suite #240 San Francisco, CA 94107
dorwick@brvatw.com
brvatw.com
looking for a water mark on the business cards and stationary. Check out the brief for the logo for more ideas. http://orders.markcraftdepot.com/contests/bright-relay-ventures/readbrief

```html
<!DOCTYPE html>
<html lang="en">
<head>
<meta charset="utf-8">
<title>BRV Stationary – Business Cards</title>
<link href="https://fonts.googleapis.com/css2?family=Roboto+Condensed:wght@400;700&display=swap" rel="stylesheet">
<style>
  :root {
    --page-bg: #d9d9d7;
    --card-white: #ffffff;
    --brand-blue: #3a5ba0;
    --brand-green: #5e9a2f;
    --ink-grey: #6b6b6b;
    --shadow: rgba(0, 0, 0, 0.28);
  }
  * { box-sizing: border-box; margin: 0; padding: 0; }
  html, body {
    width: 1200px;
    height: 980px;
    overflow: hidden;
    background: var(--page-bg);
    font-family: "Roboto Condensed", "Arial Narrow", sans-serif;
  }
  .stage { position: relative; width: 1200px; height: 980px; }

  .card {
    position: absolute;
    box-shadow: 0 8px 22px var(--shadow);
  }

  /* Front card */
  .card-front {
    left: 80px; top: 70px;
    width: 560px; height: 320px;
    background: var(--card-white);
  }
  .card-front .edge-tab {
    position: absolute;
    right: 0; top: 22px;
    width: 8px; height: 62px;
    background: var(--brand-blue);
  }
  .brand-lockup {
    position: absolute;
    left: 40px; top: 96px;
    display: flex; align-items: center; gap: 12px;
  }
  .brand-square {
    width: 18px; height: 18px;
    background: var(--brand-green);
  }
  .brand-name {
    font-weight: 700;
    font-size: 78px;
    line-height: 1;
    color: var(--brand-blue);
    letter-spacing: 1px;
  }
  .person {
    position: absolute;
    right: 32px; top: 30px;
    text-align: right;
    color: var(--brand-blue);
  }
  .person-name { font-size: 30px; line-height: 1.05; }
  .person-title { font-size: 17px; letter-spacing: 0.5px; }

  .address {
    position: absolute;
    right: 32px; top: 178px;
    width: 250px;
    font-size: 13px;
    line-height: 1.5;
    color: var(--ink-grey);
  }
  .label { color: var(--brand-green); }

  .contact-line {
    position: absolute;
    left: 40px; bottom: 28px;
    font-size: 13px;
    color: var(--ink-grey);
    letter-spacing: 0.2px;
  }
  .contact-line .sep { margin: 0 5px; }

  /* Back cards */
  .card-back {
    display: flex; flex-direction: column;
    align-items: center; justify-content: center;
    color: var(--card-white);
  }
  .card-back .brand-name { color: var(--card-white); font-size: 74px; }
  .card-back .web {
    margin-top: 8px;
    font-size: 14px;
    letter-spacing: 0.4px;
  }
  .card-green {
    left: 620px; top: 380px;
    width: 500px; height: 286px;
    background: var(--brand-green);
  }
  .card-blue {
    left: 80px; top: 560px;
    width: 540px; height: 310px;
    background: var(--brand-blue);
  }
</style>
</head>
<body>
<main class="stage">

  <section class="card card-front" aria-label="Business card front">
    <div class="edge-tab"></div>
    <div class="brand-lockup">
      <span class="brand-name">BRV</span>
      <span class="brand-square"></span>
    </div>
    <div class="person">
      <p class="person-name">Dale Orwick</p>
      <p class="person-title">CEO</p>
    </div>
    <p class="address">
      <span class="label">Add.</span> 2380 Tallow St. Suite #240<br>
      San Francisco, CA 94107
    </p>
    <p class="contact-line">
      <span class="label">P</span> 415-555-0142<span class="sep">|</span><span class="label">F</span> 415-555-0187<span class="sep">|</span><span class="label">E</span> dorwick@brvatw.com
    </p>
  </section>

  <section class="card card-back card-green" aria-label="Business card back, green">
    <span class="brand-name">BRV</span>
    <p class="web">www.brvatw.com</p>
  </section>

  <section class="card card-back card-blue" aria-label="Business card back, blue">
    <span class="brand-name">BRV</span>
    <p class="web">www.brvatw.com</p>
  </section>

</main>
</body>
</html>
```